Business Card Design

New business card design

Target Market(s)

Residential & Commercial Property Managers

Industry/Entity Type

Plumbing Services

Contact Information for Business Card

Name - Owen Tredgold, title - Director, Phone Number - 0431 862 507, email - owen@rvb-plumbing.com.au, Company ABN - 73 215 904 386,

Font styles to use
Sans Serif

Colors
0054AA
0677BA
7BADD7
CADEEF
E8F1F8

```html
<!DOCTYPE html>
<html lang="en">
<head>
<meta charset="utf-8">
<title>RVB Plumbing Services – Business Card</title>
<link href="https://fonts.googleapis.com/css2?family=Exo+2:wght@400&display=swap" rel="stylesheet">
<style>
  :root {
    --bg: #e6e8eb;
    --card: #ffffff;
    --ink: #1c1d20;
    --blue: #2aa6e0;
    --shadow: rgba(20, 24, 30, 0.18);
  }
  * { box-sizing: border-box; margin: 0; padding: 0; }
  html, body {
    width: 1200px; height: 1200px; overflow: hidden;
    background: var(--bg);
    font-family: "Exo 2", sans-serif;
    font-weight: 400;
  }
  .sheet {
    width: 1200px; height: 1200px;
    display: flex; flex-direction: column;
    align-items: center; justify-content: center; gap: 60px;
  }
  .card {
    position: relative;
    width: 840px; height: 480px;
    background: var(--card);
    box-shadow: 0 10px 30px var(--shadow);
  }
  .brand-name {
    position: absolute;
    color: var(--ink);
    font-weight: 400;
    line-height: 1;
    white-space: nowrap;
  }

  /* back */
  .card-back .brand-name {
    left: 50%; top: 170px; transform: translateX(-50%);
    font-size: 40px;
  }
  .card-back .contact-email {
    position: absolute; left: 220px; top: 330px;
  }

  /* front */
  .card-front .brand-name {
    left: 400px; top: 120px;
    font-size: 32px;
  }
  .person {
    position: absolute; left: 72px; top: 140px;
  }
  .person-name { color: var(--blue); font-size: 28px; letter-spacing: 1px; }
  .person-role { color: var(--ink); font-size: 22px; margin-top: 2px; letter-spacing: 1px; }
  .divider {
    position: absolute; left: 360px; top: 250px;
    width: 2px; height: 150px; background: var(--ink);
  }
  .contacts {
    position: absolute; left: 400px; top: 268px;
    display: flex; flex-direction: column; gap: 12px;
  }
  .contact {
    display: flex; align-items: center; gap: 10px;
    font-size: 21px; color: var(--ink); letter-spacing: 0.5px;
  }
  .contact svg { width: 20px; height: 20px; flex: none; }
</style>
</head>
<body>
<main class="sheet">

  <section class="card card-back" aria-label="Business card back">
    <div class="brand-name">RVB Plumbing Services</div>
    <div class="contact contact-email">
      <svg viewBox="0 0 20 20" aria-hidden="true"><rect x="1" y="4" width="18" height="12" fill="var(--blue)"/><path d="M1 4 L10 11 L19 4 M1 16 L8 9.5 M19 16 L12 9.5" stroke="#fff" stroke-width="1.5" fill="none"/></svg>
      <span>owen@rvb-plumbing.com.au</span>
    </div>
  </section>

  <section class="card card-front" aria-label="Business card front">
    <div class="person">
      <div class="person-name">Owen Tredgold</div>
      <div class="person-role">Director</div>
    </div>
    <div class="brand-name">RVB Plumbing Services</div>
    <div class="divider"></div>
    <div class="contacts">
      <div class="contact">
        <svg viewBox="0 0 20 20" aria-hidden="true"><path d="M6 2 C3 3 2 6 4 10 C6 14 10 17 14 18 C16 18 18 16 17 14 L14 12 L12 14 C10 13 7 10 6 8 L8 6 Z" fill="var(--blue)"/></svg>
        <span>0431 862 507</span>
      </div>
      <div class="contact">
        <svg viewBox="0 0 20 20" aria-hidden="true"><rect x="1" y="4" width="18" height="12" fill="var(--blue)"/><path d="M1 4 L10 11 L19 4 M1 16 L8 9.5 M19 16 L12 9.5" stroke="#fff" stroke-width="1.5" fill="none"/></svg>
        <span>owen@rvb-plumbing.com.au</span>
      </div>
      <div class="contact"><span>Company ABN - 73 215 904 386</span></div>
    </div>
  </section>

</main>
</body>
</html>
```